The Brambury Firm

We need a new design for our letterhead and envelopes. We are a personal injury and criminal defense firm so we need something modern and clean, but more on the professional/traditional side. Our new logo has two colors and is attached to the file so we need something that works well with those colors/matches the design. The following information needs to be on the letterhead:
Phone: (555) 314-7265
Fax: (555) 419-6032
Toll-Free: (555) 736-1149
Post Office Box 4273
Fernwick, TQ 29458-4273
TQHarmClaimsDesk.example
PalmettoShieldCounsel.example

Target Market(s)

Clients, government agencies, other law firms

Industry/Entity Type

Legal

Font styles to use
Sans Serif
Other font styles liked:
• Arial

Colors

Designer to choose colors to be used in the design.

Requirements
Must have
• Must look professional and clean, modern
Nice to have
• I would like to see a design that works with the logo but does not distract from the content that will be printed on it
Should not have
• Too many colors or crazy designs.

```html
<!DOCTYPE html>
<html lang="en">
<head>
<meta charset="utf-8">
<title>The Brambury Firm — Stationery</title>
<link href="https://fonts.googleapis.com/css2?family=Jost:wght@400;500&family=Roboto:wght@400&display=swap" rel="stylesheet">
<style>
  :root{
    --backdrop:#dcdcdc;
    --paper:#ededed;
    --paper-light:#f7f7f7;
    --navy:#2e3191;
    --red:#d31f26;
    --ink:#3f3f3f;
    --muted:#555;
  }
  *{margin:0;padding:0;box-sizing:border-box}
  html,body{width:1200px;height:877px;overflow:hidden;background:var(--backdrop)}
  .canvas{position:relative;width:1200px;height:877px;font-family:"Jost",sans-serif;color:var(--ink)}
  .sheet{position:absolute;background:linear-gradient(90deg,var(--paper-light),var(--paper) 70%);box-shadow:0 2px 8px rgba(0,0,0,.12)}
  .edge-stripes{position:absolute;left:0;top:0;bottom:0;width:9px;background:linear-gradient(90deg,var(--navy) 0 5px,var(--red) 5px 9px)}

  .letterhead{left:69px;top:64px;width:527px;height:742px}
  .brand-name{position:absolute;font-family:"Jost",sans-serif;font-weight:500;white-space:nowrap;letter-spacing:.5px}
  .letterhead .brand-name{left:39px;top:64px;font-size:22px;color:var(--red)}
  .contact-block{position:absolute;left:371px;top:56px;padding-left:10px;border-left:1px solid #c9c9c9;font-family:"Roboto",sans-serif;font-size:7.8px;line-height:9.8px;color:var(--muted);font-style:normal}
  .contact-block .addr{margin-bottom:1px}
  .contact-row{display:flex;align-items:center;gap:4px}
  .contact-row svg{width:7px;height:7px;fill:var(--navy)}
  .salutation{position:absolute;left:45px;top:208px;font-size:13.5px;font-weight:400;color:#444}
  .letter-body{position:absolute;left:45px;top:249px;width:441px;font-size:7.3px;line-height:11.4px;color:#4a4a4a}
  .letter-body p{margin-bottom:11.4px}
  .closing{position:absolute;left:45px;top:488px;font-size:7.6px;color:#4a4a4a}
  .signature{position:absolute;left:41px;top:516px;width:94px;height:38px;border-radius:4px;background:linear-gradient(90deg,rgba(31,63,154,.25),rgba(31,63,154,.12))}

  .envelope{position:absolute;width:531px;height:240px;background:linear-gradient(90deg,var(--paper-light),#e6e6e6);box-shadow:0 1px 5px rgba(0,0,0,.12)}
  .envelope .flap{position:absolute;left:0;top:0;width:531px;height:74px}
  .envelope .brand-name{font-size:13px;color:#fff;transform:translateX(-50%)}
  .envelope-back{left:645px;top:190px}
  .envelope-back .brand-name{left:265px;top:29px}
  .envelope-front-flap{left:611px;top:281px;height:241px}
  .envelope-front-flap .brand-name{left:265px;top:29px}

  .envelope-face{left:614px;top:562px;width:533px;height:242px}
  .return-address{position:absolute;left:32px;top:30px;font-family:"Roboto",sans-serif;font-size:7.8px;line-height:9.6px;color:var(--muted);font-style:normal}
</style>
</head>
<body>
<div class="canvas">

  <section class="sheet letterhead">
    <div class="edge-stripes"></div>
    <div class="brand-name">The Brambury Firm</div>
    <address class="contact-block">
      <div class="addr">Post Office Box 4273<br>Fernwick, TQ 29458-4273</div>
      <div class="contact-row"><svg viewBox="0 0 10 10"><path d="M2 0.5 3.8 2.6 2.9 3.8Q4 6 6.2 7.1L7.4 6.2 9.5 8 8.2 9.5Q4.5 9.5 0.5 1.8Z"/></svg>(555) 314-7265</div>
      <div class="contact-row"><svg viewBox="0 0 10 10"><rect x="2.5" y="0.5" width="5" height="3"/><rect x="0.5" y="4" width="9" height="4" rx="1"/><rect x="2.5" y="7" width="5" height="2.5"/></svg>(555) 419-6032</div>
      <div class="contact-row"><svg viewBox="0 0 10 10"><circle cx="5" cy="5" r="4.5"/></svg>TQHarmClaimsDesk.example</div>
      <div class="contact-row"><svg viewBox="0 0 10 10"><circle cx="5" cy="5" r="4.5"/></svg>PalmettoShieldCounsel.example</div>
    </address>

    <h1 class="salutation">Dear Mr. Hollis,</h1>
    <div class="letter-body">
      <p>Lorem ipsum dolor sit amet, consectetur adipiscing elit. Donec orci purus, luctus vitae dignissim eu, iaculis sed purus. Vivamus faucibus, ipsum nec aliquet viverra, leo mauris condimentum ligula, sit amet sagittis enim ligula quis arcu. Nam egestas tortor id nisi porttitor mattis. In tortor ante, ultricies in suscipit a, tempus non massa. Vivamus et auctor mi. Fusce vel massa nulla. Phasellus nec eros mauris, et scelerisque orci.</p>
      <p>Donec malesuada orci vitae nulla accumsan porta a id massa. Quisque accumsan iaculis magna sit amet fringilla. Maecenas consequat, magna eget tincidunt semper, odio nibh rutrum mi, id feugiat ante nisi eu risus. Vestibulum nunc orci, rhoncus a placerat in, ultricies in mi. Cras mattis varius eros, vel fringilla nisi suscipit eget. Quisque scelerisque sagittis nulla at porttitor.</p>
      <p>Sed id augue vitae urna euismod commodo aliquet a quam. Pellentesque arcu velit, cursus et malesuada ut, consequat et diam. Nullam erat sem, rhoncus id ullamcorper vitae, rhoncus et arcu. In ultricies ultricies nulla, ut rutrum nisi iaculis at. Donec eu magna a metus ornare faucibus. Fusce aliquet faucibus ultricies. Morbi semper, est id tincidunt gravida, sem arcu adipiscing lacus, ac bibendum nulla leo eu purus. Quisque nec diam sed risus consectetur a ccumsan quis quis nibh. Vestibulum id purus lorem.</p>
      <p>It is a long established fact that a reader will be distracted by the readable content of a page when looking at its layout. The point of using Lorem Ipsum is that it has a more-or-less normal distribution of letters, as opposed to using 'Content here, content here', making it look like readable English. Many desktop publishing packages</p>
    </div>
    <div class="closing">Sincerely,</div>
    <div class="signature" role="img" aria-label="Handwritten signature of the sender in blue ink"></div>
  </section>

  <section class="envelope envelope-back">
    <svg class="flap" viewBox="0 0 531 74"><path d="M0 0H531L520 50Q514 74 490 74H41Q17 74 11 50Z" fill="var(--red)"/></svg>
    <div class="brand-name">The Brambury Firm</div>
  </section>

  <section class="envelope envelope-front-flap">
    <svg class="flap" viewBox="0 0 531 74"><path d="M0 0H531L520 50Q514 74 490 74H41Q17 74 11 50Z" fill="var(--navy)"/></svg>
    <div class="brand-name">The Brambury Firm</div>
  </section>

  <section class="sheet envelope-face">
    <div class="edge-stripes"></div>
    <address class="return-address">Post Office Box 4273<br>Fernwick, TQ 29458-4273</address>
  </section>

</div>
</body>
</html>
```